Business Card Design Project

need some business cards with the logo provided. I am a manufacturing jeweller that make high end quality jewellery in silver, gold and platinum and some amazing colored stones and of course diamonds.
Updates

Project Deadline Extended
Reason: I didn't choose this specific deadline and not sure why it was so short. A team member of craft huddle helped as i am not the best on computers. (-: (wasn't asked about the dead line)

Target Market(s)

Adults based between 20 to 60 and have budgets between $5000 - $100 000

Industry/Entity Type

Business

Colors

Designer to choose colors to be used in the design.

Requirements
Must have
• All in the front of business card
LOGO provided
My name: Corinne Walbeck
Job: Manufacturing jeweller
Phone number: 047 215 3904
Email: walcor@fernmail.example and the pagewave logo
this all in the back:
description of what i do : Hand Made Jewellery
new designs, remodelling, bridal jewellery, pearl re-threading and repairs
PO Box 1735, Larkfield, 6412
Should not have
• Any diamond shapes or diamond rings or gemstones.

```html
<!DOCTYPE html>
<html lang="en">
<head>
<meta charset="utf-8">
<title>Orvale Jewellers – Business Card</title>
<link rel="stylesheet" href="https://fonts.googleapis.com/css2?family=Montserrat:wght@400;500&family=Allura&display=swap">
<style>
  :root {
    --page: #ffffff;
    --card: #1d1f22;
    --ink: #ffffff;
    --muted: #a9abae;
    --brand: #9b9c9e;
    --floral-1: #3a3c42;
    --floral-2: #26282c;
    --chip: #8e8f92;
  }
  * { box-sizing: border-box; margin: 0; padding: 0; }
  html, body { width: 1000px; height: 1200px; overflow: hidden; background: var(--page); }
  body { position: relative; font-family: "Montserrat", Arial, sans-serif; }

  .card {
    position: absolute; left: 117px; width: 768px; height: 466px;
    background: var(--card); overflow: hidden;
  }
  .card--front { top: 119px; }
  .card--back { top: 608px; }

  .floral-area {
    position: absolute; top: 0; right: 0; width: 300px; height: 100%;
    background: linear-gradient(90deg, rgba(58,60,66,0) 0%, var(--floral-2) 35%, var(--floral-1) 100%);
  }

  .brand { position: absolute; left: 84px; top: 84px; width: 290px; text-align: center;
    color: var(--brand); font-weight: 400; text-transform: uppercase; }
  .brand__name { font-size: 62px; letter-spacing: 6px; line-height: 1; }
  .brand__sub { font-size: 20px; letter-spacing: 8px; margin-top: 14px; padding-left: 8px; }

  .person { position: absolute; right: 94px; top: 210px; text-align: right; }
  .person__name { font-family: "Allura", cursive; font-size: 44px; color: var(--ink); line-height: 1; }
  .person__role { margin-top: 17px; font-size: 17px; line-height: 18px; letter-spacing: 1px;
    color: var(--muted); text-transform: uppercase; }
  .rule { position: absolute; width: 2px; background: var(--ink); }
  .rule--front { left: 695px; top: 211px; height: 100px; }

  .contact { position: absolute; left: 87px; top: 371px; font-size: 16px; line-height: 19px; color: var(--ink); }
  .contact__label { color: var(--muted); }

  .social { position: absolute; left: 338px; top: 378px; display: flex; align-items: center; gap: 8px;
    font-size: 14px; color: var(--muted); }
  .social__chip { width: 36px; height: 37px; background: var(--chip); }

  .rule--back { left: 86px; top: 100px; height: 100px; }
  .services { position: absolute; left: 101px; top: 104px; font-size: 17.5px; line-height: 18.5px;
    color: var(--ink); text-transform: uppercase; letter-spacing: 0.3px; }
  .address { position: absolute; right: 100px; top: 366px; font-size: 17px; letter-spacing: 0.5px;
    color: var(--muted); text-transform: uppercase; }
</style>
</head>
<body>
  <section class="card card--front">
    <div class="floral-area" role="img" aria-label="Dark tonal floral vine ornament"></div>
    <div class="brand">
      <div class="brand__name">Orvale</div>
      <div class="brand__sub">Jewellers</div>
    </div>
    <div class="person">
      <div class="person__name">Corinne Walbeck</div>
      <div class="person__role">Manufacturing<br>Jeweller</div>
    </div>
    <div class="rule rule--front"></div>
    <div class="contact">
      <div><span class="contact__label">P:</span> 047 215 3904</div>
      <div><span class="contact__label">E:</span> walcor@fernmail.example</div>
    </div>
    <div class="social"><span class="social__chip"></span>pagewave</div>
  </section>

  <section class="card card--back">
    <div class="floral-area" role="img" aria-label="Dark tonal floral vine ornament"></div>
    <div class="rule rule--back"></div>
    <div class="services">
      Hand made jewellery<br>
      New designs, remodelling,<br>
      Bridal jewellery,<br>
      Pearl re-threading<br>
      and repairs
    </div>
    <div class="address">PO Box 1735, Larkfield, 6412</div>
  </section>
</body>
</html>
```